Business card por a urban DJ, up scale audience target

Need a sober design, modern, conservative colors but i can consider some options, y play rnb, hip hop, EDM and top40.

Business card for contact and personal info, double sided, use logo attrached please; im 42 so i need a card acording to my age an target audience.

Target Market(s)

Adult people, up scale audience

Industry/Entity Type

Music Download

Contact Information for Business Card

Cel (312) 555-0147 www.lumaverso.com

Requirements
Must have
• open mind
Nice to have
• open mind
Should not have
• DJ

```html
<!DOCTYPE html>
<html lang="en">
<head>
<meta charset="utf-8">
<title>Luma — Business Card</title>
<link href="https://fonts.googleapis.com/css2?family=Roboto:wght@400;700;900&display=swap" rel="stylesheet">
<style>
  :root {
    --backdrop: #2b2b2d;
    --card-white: #ffffff;
    --card-black: #0c0c0c;
    --ink: #111111;
    --band-grey: #bdbdbd;
    --panel-top: #3a3a3a;
    --panel-bottom: #141414;
    --panel-text: #f2f2f2;
    --panel-muted: #cfcfcf;
    --back-text: #d9d9d9;
  }
  * { box-sizing: border-box; margin: 0; padding: 0; }
  html, body {
    width: 1200px; height: 950px; overflow: hidden;
    background: var(--backdrop);
    font-family: "Roboto", Arial, sans-serif;
  }
  .sheet {
    width: 1200px; height: 950px;
    display: flex; flex-direction: column;
    align-items: center; justify-content: center;
    gap: 50px;
  }
  .card {
    position: relative;
    width: 700px; height: 400px;
    box-shadow: 0 12px 30px rgba(0,0,0,.45);
    overflow: hidden;
  }

  /* Front side */
  .card--front { background: var(--card-white); }
  .card__edge-band {
    position: absolute; left: 14px; top: 0; bottom: 0;
    width: 14px; background: var(--band-grey);
  }
  .card__side-band {
    position: absolute; right: 0; top: 0; bottom: 0;
    width: 340px;
    background: linear-gradient(180deg, #e9e9e9 0%, #f7f7f7 50%, #e4e4e4 100%);
  }
  .brand {
    position: absolute; left: 72px; top: 0; bottom: 0;
    display: flex; align-items: center; gap: 12px;
    color: var(--ink);
    font-weight: 900; font-size: 70px; letter-spacing: 1px; line-height: 1;
  }
  .brand__mark {
    width: 16px; height: 16px; background: var(--ink);
  }
  .contact-panel {
    position: absolute; right: 30px; top: 84px;
    width: 300px; height: 232px;
    background: linear-gradient(160deg, var(--panel-top) 0%, #222 45%, var(--panel-bottom) 100%);
    padding: 44px 28px 0 28px;
    color: var(--panel-text);
  }
  .contact-panel__name {
    font-weight: 700; font-size: 26px; letter-spacing: .5px; line-height: 1.1;
  }
  .contact-panel__role {
    font-size: 17px; letter-spacing: 1px; margin-top: 4px; color: var(--panel-muted);
  }
  .contact-panel__line {
    font-size: 19px; margin-top: 6px; color: var(--panel-muted);
  }
  .contact-panel__role + .contact-panel__line { margin-top: 22px; }

  /* Back side */
  .card--back {
    background: linear-gradient(170deg, #1b1b1b 0%, var(--card-black) 60%, #050505 100%);
    display: flex; flex-direction: column; align-items: center; justify-content: center;
    gap: 22px;
  }
  .brand--reverse {
    position: static; color: #ffffff; font-size: 100px;
  }
  .brand--reverse .brand__mark { background: #ffffff; width: 22px; height: 22px; }
  .card__web {
    color: var(--back-text); font-size: 22px; letter-spacing: 4px;
  }
</style>
</head>
<body>
<main class="sheet">
  <section class="card card--front" aria-label="Card front">
    <div class="card__edge-band"></div>
    <div class="card__side-band"></div>
    <div class="brand">
      <span class="brand__mark"></span>
      <span class="brand__name">LUMA</span>
    </div>
    <div class="contact-panel">
      <p class="contact-panel__name">MARCO REYES</p>
      <p class="contact-panel__role">PRESIDENT</p>
      <p class="contact-panel__line">(312) 555-0147</p>
      <p class="contact-panel__line">www.lumaverso.com</p>
    </div>
  </section>

  <section class="card card--back" aria-label="Card back">
    <div class="brand brand--reverse">
      <span class="brand__mark"></span>
      <span class="brand__name">LUMA</span>
    </div>
    <p class="card__web">WWW.LUMAVERSO.COM</p>
  </section>
</main>
</body>
</html>
```